hi all

Im after a new age looking business card with my company logo on it

must include these details, I would like the PH and Email to be symbols

If the colours used for card could be kept within the colours used in logo that I have supplied that would be great, if another colour is to be used dark grey would be ok. no light bulbs etc thanks

Details below to be incorporated on card

Damian Holloway

Lic E871302

PH 0219647381

E info@brightvaleelectrical.example.nz

Domestic Commercial Industrial Electricians

```html
<!DOCTYPE html>
<html lang="en">
<head>
<meta charset="utf-8">
<title>Brightvale Electrical – Business Card</title>
<link href="https://fonts.googleapis.com/css2?family=Roboto+Condensed:wght@400;700&display=swap" rel="stylesheet">
<style>
  :root {
    --card-grey: #e8e8e8;
    --bolt-grey: #d3d3d3;
    --brand-blue: #2186f8;
    --ink-dark: #1e1e1e;
    --ink-light: #ffffff;
  }
  * { margin: 0; padding: 0; box-sizing: border-box; }
  html, body {
    width: 1200px;
    height: 750px;
    overflow: hidden;
    background: var(--card-grey);
  }
  .card {
    position: relative;
    width: 1200px;
    height: 750px;
    overflow: hidden;
    font-family: "Roboto Condensed", "Arial Narrow", sans-serif;
  }
  .card-shapes {
    position: absolute;
    inset: 0;
  }
  .holder-name {
    position: absolute;
    top: 62px;
    right: 77px;
    font-size: 56px;
    font-weight: 700;
    color: var(--ink-light);
    letter-spacing: 0.2px;
  }
  .brand {
    position: absolute;
    left: 62px;
    top: 400px;
    width: 360px;
    display: flex;
    align-items: center;
    gap: 18px;
  }
  .brand-dot {
    width: 62px;
    height: 62px;
    border-radius: 50%;
    background: var(--ink-dark);
    flex: none;
  }
  .brand-name {
    font-size: 42px;
    line-height: 1.0;
    font-weight: 700;
    color: var(--brand-blue);
    letter-spacing: 2px;
  }
  .services {
    position: absolute;
    left: 55px;
    top: 618px;
    font-size: 35px;
    line-height: 52px;
    color: var(--ink-dark);
  }
  .contact {
    position: absolute;
    left: 590px;
    top: 512px;
    list-style: none;
    color: var(--ink-light);
    font-size: 38px;
    line-height: 56px;
  }
  .contact li {
    display: flex;
    align-items: center;
  }
  .contact-icon {
    width: 40px;
    height: 40px;
    margin-right: 17px;
    flex: none;
  }
  .contact-icon.blank { visibility: hidden; }
  .contact .email { font-size: 34px; }
</style>
</head>
<body>
<main class="card">
  <svg class="card-shapes" width="1200" height="750" viewBox="0 0 1200 750" aria-hidden="true">
    <rect width="1200" height="750" fill="var(--card-grey)"/>
    <polygon class="bolt" points="550,0 341,407 489,412 489,750 676,289 525,289" fill="var(--bolt-grey)"/>
    <polygon class="blue-field" points="550,0 1200,0 1200,750 489,750 676,289 525,289" fill="var(--brand-blue)"/>
  </svg>

  <h1 class="holder-name">Damian Holloway</h1>

  <div class="brand">
    <span class="brand-dot"></span>
    <span class="brand-name">BRIGHTVALE<br>ELECTRICAL</span>
  </div>

  <p class="services">Domestic Commercial<br>Industrial Electricians Files</p>

  <ul class="contact">
    <li><svg class="contact-icon blank" viewBox="0 0 40 40" aria-hidden="true"></svg>Lic E871302</li>
    <li>
      <svg class="contact-icon" viewBox="0 0 40 40" aria-label="Phone">
        <circle cx="20" cy="21" r="12" fill="none" stroke="#fff" stroke-width="2"/>
        <path d="M15 14 q-3 8 4 14 l3 -3 -3 -3 q-2 -2 -1 -5 l-3 -3z" fill="#fff"/>
      </svg>0219647381
    </li>
    <li class="email">
      <svg class="contact-icon" viewBox="0 0 40 40" aria-label="Email">
        <rect x="4" y="10" width="32" height="21" fill="none" stroke="#fff" stroke-width="2"/>
        <path d="M4 10 L20 23 L36 10 M4 31 L16 20 M36 31 L24 20" fill="none" stroke="#fff" stroke-width="2"/>
      </svg>info@brightvaleelectrical.example.nz
    </li>
  </ul>
</main>
</body>
</html>
```